Morvik Construction Business Card

I need a business card design for my company.
We are a construction/machinery company.
I would like to see my logo on the front of the card and my details on the other side
I would like the card to be black or dark grey in colour,with my logo as i send it or modified with a lighter blue colour
I would like to see the design kept fairly simple,but eye catching at the same time
Industry/Entity Type
Business
Colors
00a990
1b1b1b
000000
474747
ececec

```html
<!DOCTYPE html>
<html lang="en">
<head>
<meta charset="utf-8">
<title>Morvik Construction – Business Card</title>
<link rel="stylesheet" href="https://fonts.googleapis.com/css2?family=Roboto:wght@400;500;700&display=swap">
<style>
  :root {
    --teal: #00a990;
    --ink: #1b1b1b;
    --charcoal: #3c3d3f;
    --grey: #474747;
    --paper: #f4f4f2;
    --stage: #ececec;
  }
  * { box-sizing: border-box; margin: 0; padding: 0; }
  html, body {
    width: 1200px; height: 716px; overflow: hidden;
    background: var(--stage);
    font-family: "Roboto", Arial, sans-serif;
  }
  .canvas { position: relative; width: 1200px; height: 716px; }
  .card {
    position: absolute; top: 203px;
    width: 540px; height: 309px;
    background: var(--paper);
    overflow: hidden;
    box-shadow: 0 2px 6px rgba(0,0,0,.18);
  }
  .card--front { left: 40px; }
  .card--back { left: 620px; }

  .wordmark {
    display: flex; align-items: center; gap: 12px;
    color: var(--grey); font-weight: 700;
    letter-spacing: .5px; white-space: nowrap;
  }
  .wordmark__square { width: 22px; height: 22px; background: var(--grey); flex: none; }
  .card--front .wordmark {
    position: absolute; left: 50%; top: 50%;
    transform: translate(-50%, -50%);
    font-size: 30px;
  }
  .card--back .wordmark {
    position: absolute; left: 40px; top: 42px;
    font-size: 26px;
  }

  .contact {
    position: absolute; left: 40px; top: 100px;
    list-style: none; font-size: 12.5px; color: var(--ink);
    line-height: 19px;
  }
  .contact__address { padding-left: 22px; }
  .contact li { display: flex; align-items: center; gap: 8px; }
  .contact svg { width: 14px; height: 14px; fill: var(--teal); flex: none; }

  .wave { position: absolute; left: 0; top: 0; width: 540px; height: 309px; }
  .holder {
    position: absolute; right: 34px; bottom: 24px; text-align: right;
  }
  .holder__name { color: var(--teal); font-weight: 700; font-size: 21px; }
  .holder__title { color: #fff; font-size: 13px; margin-top: 4px; }
</style>
</head>
<body>
<main class="canvas">

  <section class="card card--front" aria-label="Card front">
    <div class="wordmark"><span class="wordmark__square"></span>Morvik Construction</div>
  </section>

  <section class="card card--back" aria-label="Card back">
    <svg class="wave" viewBox="0 0 540 309" aria-hidden="true">
      <path d="M0,194 C150,186 260,212 385,198 C455,190 505,184 540,180" fill="none" stroke="var(--teal)" stroke-width="2"/>
      <path d="M0,204 C150,196 260,222 385,208 C455,200 505,194 540,190 L540,199 C505,203 455,209 385,218 C260,232 150,206 0,214 Z" fill="var(--teal)"/>
      <path d="M0,226 C150,218 260,238 385,224 C455,216 505,208 540,204 L540,309 L0,309 Z" fill="var(--charcoal)"/>
    </svg>

    <div class="wordmark"><span class="wordmark__square"></span>Morvik Construction</div>

    <ul class="contact">
      <li class="contact__address">Your Long Commercial address, Code</li>
      <li>
        <svg viewBox="0 0 24 24"><path d="M6.6 10.8a15 15 0 0 0 6.6 6.6l2.2-2.2c.3-.3.7-.4 1-.2 1.1.4 2.3.6 3.6.6.6 0 1 .4 1 1V20c0 .6-.4 1-1 1A17 17 0 0 1 3 4c0-.6.4-1 1-1h3.5c.6 0 1 .4 1 1 0 1.3.2 2.5.6 3.6.1.3 0 .7-.2 1z"/></svg>
        +00 111 222 3333
      </li>
      <li>
        <svg viewBox="0 0 24 24"><path d="M2 5h20v14H2z M4 7v1l8 5 8-5V7l-8 5z" fill-rule="evenodd"/></svg>
        www.yourwebsite.com
      </li>
      <li>
        <svg viewBox="0 0 24 24"><circle cx="12" cy="12" r="10"/><circle cx="12" cy="12" r="4" fill="var(--paper)"/></svg>
        yourname@yourwebsite.com
      </li>
    </ul>

    <div class="holder">
      <div class="holder__name">Your Good Name</div>
      <div class="holder__title">General Contractor</div>
    </div>
  </section>

</main>
</body>
</html>
```